Velmora ICT is an ICT Project Services, ICT Architecture and Cloud consultation service business. I need a web site that is simple and looks professional and can grow with my business. I'll leave the creativity and colours up to you as the creative professionals.
Our ICT Project Services specialise in small to medium ICT Projects for government agencies and private organisations and Defence. Our project consultancy services helps our clients get to project execution, Projects as a Service. More information on the offering to be provided.
Cloud services consultation aide and manage in getting clients into the cloud, utilising our technical experience and project management.
I need additional tabs on the site to cater for my additional services.
I am about to offer Quorvane Cloud Certification which will be a paid monthly subscription.
I also require a tab that focuses on our developed Project software. Project as a service. Essentially a step by step application that controls and runs the project from execution to closure for small (complex service requests) projects under $100000.
Happy to provide much more information.
Target Market(s)
Small to medium business, government agencies
Industry/Entity Type
It Company
Contact Information for Business Card
Velmora ICT
Business Project Management and Architectural Services
Project Management as a Service.
Logo Text
Velmora ICT Consultative Business, Project Management and Architectural Services
2 page
Requirements
Must have
- Additional tabs for the additional products ICT Training and Project Management Applicaiton

```html
<!DOCTYPE html>
<html lang="en">
<head>
<meta charset="utf-8">
<title>Velmora ICT – Architecture and Cloud Consultation Service</title>
<link href="https://fonts.googleapis.com/css2?family=Open+Sans:wght@300;400;600;700&display=swap" rel="stylesheet">
<style>
:root{
  --navy:#0b3d5c;
  --navy-deep:#023f5f;
  --accent:#1e88c7;
  --bar:#0f5a82;
  --text:#6d6d6d;
  --rule:#dcdcdc;
  --services-bg:#f3f2f3;
  --testimonials-bg:#ebebec;
  --white:#ffffff;
}
*{box-sizing:border-box;margin:0;padding:0}
html,body{width:1200px;height:2365px;overflow:hidden}
body{font-family:"Open Sans",Arial,sans-serif;background:var(--white);position:relative;color:var(--text)}
.abs{position:absolute}

/* header */
.site-header{position:absolute;left:0;top:0;width:1200px;height:79px;background:var(--white)}
.brand{position:absolute;left:31px;top:14px;font-size:38px;font-weight:400;color:var(--navy);letter-spacing:.5px}
.main-nav{position:absolute;top:22px;left:0;width:1200px;height:30px}
.main-nav a{position:absolute;top:0;height:30px;line-height:30px;font-size:14px;font-weight:700;color:var(--navy);text-decoration:none;text-transform:uppercase;letter-spacing:.3px}
.main-nav a.is-active{background:var(--accent);color:var(--white);padding:0 10px;border-radius:3px}

/* hero */
.hero{position:absolute;left:0;top:79px;width:1200px;height:563px;background:linear-gradient(180deg,#4a4a4e 0%,#3b3a3d 45%,#2e2e33 100%)}
.hero-photo{position:absolute;inset:0;background:linear-gradient(90deg,rgba(60,58,62,.9),rgba(90,84,86,.6) 50%,rgba(55,55,62,.9))}
.hero-title{position:absolute;left:0;width:1200px;text-align:center;font-weight:700;font-size:56px;letter-spacing:.5px;line-height:1}
.hero-title.line-one{top:218px;color:var(--accent)}
.hero-title.line-two{top:292px;color:var(--white)}

/* section headings */
.section-heading{position:absolute;left:31px;font-size:30px;font-weight:700;color:var(--navy);text-transform:uppercase;line-height:1}
.section-rule{position:absolute;height:3px;background:var(--rule)}

/* about */
.about-photo{position:absolute;left:30px;top:771px;width:441px;height:278px;background:linear-gradient(135deg,#cdd9e4 0%,#8c9bab 45%,#3f4c5c 100%)}
.about-copy{position:absolute;left:571px;width:582px;font-size:15px;line-height:23.7px;color:var(--text)}
.btn{position:absolute;background:var(--navy);color:var(--white);font-weight:700;text-transform:uppercase;text-align:center;text-decoration:none}
.btn-more{left:757px;top:1006px;width:165px;height:44px;line-height:44px;font-size:24px}

/* services */
.services{position:absolute;left:0;top:1099px;width:1200px;height:631px;background:var(--services-bg)}
.service-photo{position:absolute;top:1227px;width:357px;height:218px}
.service-title{position:absolute;top:1471px;font-size:16.5px;font-weight:700;color:var(--navy)}
.service-copy{position:absolute;top:1508px;width:360px;font-size:14.3px;line-height:23.7px;color:var(--text)}
.btn-read{top:1645px;width:137px;height:43px;line-height:43px;font-size:14px}

/* testimonials */
.testimonials{position:absolute;left:0;top:1730px;width:1200px;height:355px;background:var(--testimonials-bg)}
.avatar{position:absolute;width:88px;height:88px;border-radius:50%;background:radial-gradient(circle at 50% 40%,#d9e9f2,#a7c7da)}
.testimonial-name{position:absolute;top:1960px;width:380px;text-align:center;font-size:12.5px;color:var(--navy);text-transform:uppercase}
.testimonial-copy{position:absolute;top:1985px;width:380px;text-align:center;font-size:12px;line-height:18px;color:var(--text)}

/* footer */
.site-footer{position:absolute;left:0;top:2085px;width:1200px;height:233px;background:var(--navy-deep);color:var(--white)}
.footer-heading{position:absolute;top:50px;font-size:14px;font-weight:400;color:var(--white)}
.contact-line{position:absolute;left:123px;font-size:12.5px;font-weight:600}
.contact-icon{position:absolute;left:69px}
.social{position:absolute;top:73px;width:22px;height:22px;border-radius:50%;background:var(--white)}
.follow-copy{position:absolute;left:313px;top:108px;width:200px;font-size:11.5px;line-height:18px}
.field{position:absolute;left:954px;width:178px;height:27px;border:1px solid #3f86ad;background:#0c5479;color:var(--white);font-size:11.5px;line-height:25px;padding-left:9px}
.subscribe{position:absolute;left:954px;top:151px;width:77px;height:25px;border:1px solid #3f86ad;background:#0c5479;font-size:11px;line-height:23px;text-align:center}
.copyright-bar{position:absolute;left:0;top:2318px;width:1200px;height:47px;background:var(--bar);color:var(--white);text-align:center;font-size:14px;line-height:47px}
</style>
</head>
<body>

<header class="site-header">
  <div class="brand">Velmora ICT</div>
  <nav class="main-nav">
    <a class="is-active" style="left:551px">Home</a>
    <a style="left:640px">About Us</a>
    <a style="left:747px">ICT Training</a>
    <a style="left:878px">Project Management</a>
    <a style="left:1079px">Contact Us</a>
  </nav>
</header>

<section class="hero">
  <div class="hero-photo" role="img" aria-label="Group photo of smiling business professionals standing together in an office"></div>
  <h1 class="hero-title line-one">ARCHITECTURE AND CLOUD</h1>
  <h1 class="hero-title line-two">CONSULTATION SERVICE</h1>
</section>

<h2 class="section-heading" style="top:692px">About Us</h2>
<div class="section-rule" style="left:205px;top:705px;width:965px"></div>
<div class="about-photo" role="img" aria-label="Business people shaking hands across a meeting table"></div>
<p class="about-copy" style="top:763px">Lorem Ipsum is simply dummy text of the printing and typesetting industry. Lorem Ipsum has been the industry's standard dummy text ever since the 1500s, when an unknown printer took a galley of type and scrambled it to make a type specimen book. It has survived not only five centuries, but also the leap into electronic typesetting, remaining essentially unchanged. It was popularised in the 1960s with the release of Letraset sheets containing</p>
<p class="about-copy" style="top:903px">Lorem Ipsum is simply dummy text of the printing and typesetting industry. Lorem Ipsum has been the industry's standard dummy text ever since the 1500s, when an unknown printer took a galley of type and scrambled it to make a type specimen book.</p>
<a class="btn btn-more">More</a>

<section class="services"></section>
<h2 class="section-heading" style="top:1151px;left:29px">Our Services</h2>
<div class="section-rule" style="left:255px;top:1164px;width:913px"></div>

<div class="service-photo" style="left:32px;background:linear-gradient(180deg,#9c8a74 0%,#3a3f4f 55%,#c4864a 100%)" role="img" aria-label="Officials seated at a press conference table"></div>
<div class="service-photo" style="left:421px;background:linear-gradient(135deg,#a59b88 0%,#4b4a4c 55%,#2b2d33 100%)" role="img" aria-label="Business colleagues reviewing a laptop together"></div>
<div class="service-photo" style="left:812px;background:linear-gradient(135deg,#5c6248 0%,#8a8a6e 45%,#3b3d36 100%)" role="img" aria-label="Defence personnel working with field equipment"></div>

<h3 class="service-title" style="left:30px">ICT Projects For Government Agencies</h3>
<h3 class="service-title" style="left:421px">ICT Projects For Private Organisations</h3>
<h3 class="service-title" style="left:812px">ICT Projects For Defence</h3>

<p class="service-copy" style="left:30px">Lorem Ipsum is simply dummy text of the printing and typesetting industry. Lorem Ipsum has been the industry's standard dummy text ever since the 1500s, when an unknown printer took a galley of type and scrambled it to make a type specimen book.</p>
<p class="service-copy" style="left:420px">Lorem Ipsum is simply dummy text of the printing and typesetting industry. Lorem Ipsum has been the industry's standard dummy text ever since the 1500s, when an unknown printer took a galley of type and scrambled it to make a type specimen book.</p>
<p class="service-copy" style="left:811px">Lorem Ipsum is simply dummy text of the printing and typesetting industry. Lorem Ipsum has been the industry's standard dummy text ever since the 1500s, when an unknown printer took a galley of type and scrambled it to make a type specimen book.</p>

<a class="btn btn-read" style="left:141px">Read More</a>
<a class="btn btn-read" style="left:531px">Read More</a>
<a class="btn btn-read" style="left:922px">Read More</a>

<section class="testimonials"></section>
<h2 class="section-heading" style="top:1779px">Testimonials</h2>
<div class="section-rule" style="left:272px;top:1792px;width:897px"></div>

<div class="avatar" style="left:344px;top:1854px" role="img" aria-label="Portrait of client Owen Hale"></div>
<div class="avatar" style="left:814px;top:1854px" role="img" aria-label="Portrait of client Lina Marsh"></div>
<div class="testimonial-name" style="left:197px">Owen Hale</div>
<div class="testimonial-name" style="left:667px">Lina Marsh</div>
<p class="testimonial-copy" style="left:197px">Lorem Ipsum is simply dummy text of the printing and typesetting industry. Lorem Ipsum has been the industry's standard dummy text ever since the 1500s,</p>
<p class="testimonial-copy" style="left:667px">Lorem Ipsum is simply dummy text of the printing and typesetting industry. Lorem Ipsum has been the industry's standard dummy text ever since the 1500s,</p>

<footer class="site-footer">
  <h4 class="footer-heading" style="left:69px">Contact Info</h4>
  <svg class="contact-icon" style="top:86px" width="18" height="24" viewBox="0 0 18 24" fill="none" stroke="#fff" stroke-width="1.6"><path d="M9 23C9 23 2 14 2 8.5a7 7 0 0 1 14 0C16 14 9 23 9 23z"/><circle cx="9" cy="8.5" r="2.6"/></svg>
  <div class="contact-line" style="top:89px">Address</div>
  <svg class="contact-icon" style="top:127px" width="22" height="22" viewBox="0 0 22 22" fill="none" stroke="#fff" stroke-width="1.6"><circle cx="11" cy="11" r="9.5"/><path d="M7.5 6.5l2 2-1.2 1.4a6 6 0 0 0 3.8 3.8l1.4-1.2 2 2-1.3 1.3c-3.5 0-7.3-3.8-7.3-7.3z"/></svg>
  <div class="contact-line" style="top:129px">000+4817+3390</div>
  <svg class="contact-icon" style="top:170px" width="22" height="15" viewBox="0 0 22 15" fill="none" stroke="#fff" stroke-width="1.4"><rect x="1" y="1" width="20" height="13"/><path d="M1 1l10 7 10-7M1 14l7-6M21 14l-7-6"/></svg>
  <div class="contact-line" style="top:169px">info@velmoraict.com</div>

  <h4 class="footer-heading" style="left:313px">Follow Us</h4>
  <div class="social" style="left:315px"></div>
  <div class="social" style="left:348px"></div>
  <p class="follow-copy">Our New products in the US market myself out with my new page thing. Feel free to show me</p>

  <h4 class="footer-heading" style="left:621px">Download Product Catalogue</h4>
  <svg class="abs" style="left:623px;top:78px" width="28" height="22" viewBox="0 0 28 22"><path d="M1 4h9l3 3h14v14H1z" fill="#f0a030"/><path d="M14 9v8M10 13l4 4 4-4" stroke="#fff" stroke-width="2" fill="none"/></svg>

  <h4 class="footer-heading" style="left:954px;top:51px">Newsletter Updates</h4>
  <div class="field" style="top:82px">enter your name</div>
  <div class="field" style="top:115px">enter your Email</div>
  <div class="subscribe">Subscribe</div>
</footer>
<div class="copyright-bar">Velmora ICT @All Rights Reserved 2016</div>

</body>
</html>
```